Veltrane Industrial Coatings

We are looking to improve our business cards. Our company installs industrial floor and wall coatings in industrial, chemical and food processing plants.
Our coatings which consist of epoxy, urethane, and vinyl esters provide chemical and abrasion resistant surface with non-skid properties that are easy to clean.

Target Market(s)

food manufacturing, chemical plants, breweries and wineries, warehouses, clean room floors.

Industry/Entity Type

Construction

Contact Information for Business Card

improved current logo.

Colors

Designer to choose colors to be used in the design.

Requirements
Must have
• the information from uploaded file
Nice to have
• "We'll be outstanding on your floors."

```html
<!DOCTYPE html>
<html lang="en">
<head>
<meta charset="utf-8">
<title>Veltrane Inc. Business Cards</title>
<link rel="stylesheet" href="https://fonts.googleapis.com/css2?family=Roboto+Slab:wght@400;700&family=Lato:wght@400;700&display=swap">
<style>
  :root {
    --canvas: #e9e7e3;
    --charcoal: #3a3a3a;
    --ink: #333333;
    --paper: #ffffff;
    --marker: #b5b5b5;
    --stripe: #a9a9a9;
    --soft-white: #f2f2f2;
  }
  * { box-sizing: border-box; margin: 0; padding: 0; }
  html, body { width: 1200px; height: 900px; overflow: hidden; }
  body {
    background: var(--canvas);
    position: relative;
    font-family: "Lato", Arial, sans-serif;
  }
  .card {
    position: absolute;
    top: 296px;
    width: 540px;
    height: 309px;
    overflow: hidden;
    box-shadow: 0 6px 18px rgba(0,0,0,0.18);
  }
  .card-front { left: 40px; background: var(--charcoal); }
  .card-back { left: 620px; background: var(--paper); }

  .brand-name {
    font-family: "Roboto Slab", Georgia, serif;
    font-weight: 400;
    line-height: 1;
    white-space: nowrap;
  }
  .brand-marker {
    flex: none;
    border-radius: 50%;
    background: var(--marker);
  }

  /* Front */
  .brand-lockup {
    position: absolute;
    left: 0; right: 0;
    top: 98px;
    display: flex;
    justify-content: center;
    align-items: center;
    gap: 14px;
  }
  .brand-lockup .brand-marker { width: 14px; height: 14px; }
  .brand-lockup .brand-name { font-size: 36px; color: var(--paper); }
  .brand-sub {
    text-align: right;
    font-family: "Lato", Arial, sans-serif;
    font-size: 8.5px;
    letter-spacing: 0.6px;
    color: var(--soft-white);
    margin-top: 5px;
  }
  .front-tagline {
    position: absolute;
    left: 0; right: 0;
    bottom: 40px;
    text-align: center;
    font-family: "Roboto Slab", Georgia, serif;
    font-size: 12px;
    letter-spacing: 0.4px;
    color: var(--soft-white);
  }

  /* Back */
  .swoosh { position: absolute; inset: 0; width: 540px; height: 309px; }
  .contact-name {
    position: absolute; left: 34px; top: 30px;
    font-family: "Roboto Slab", Georgia, serif;
    font-weight: 700;
    font-size: 19px;
    color: var(--ink);
    line-height: 1;
  }
  .contact-tollfree {
    position: absolute; left: 40px; top: 52px;
    font-size: 13px; color: var(--ink);
  }
  .contact-address {
    position: absolute; left: 52px; top: 92px;
    font-size: 15px; line-height: 19px; color: var(--ink);
  }
  .contact-list {
    position: absolute; left: 56px; top: 146px;
    list-style: none;
  }
  .contact-list li {
    display: flex; align-items: center;
    font-size: 15px; line-height: 19px; color: var(--ink);
  }
  .contact-list svg { width: 13px; height: 13px; margin-right: 6px; fill: var(--ink); flex: none; }
  .back-brand {
    position: absolute; right: 30px; top: 50px;
    display: flex; align-items: center; gap: 12px;
  }
  .back-brand .brand-marker { width: 12px; height: 12px; background: #c4c4c4; }
  .back-brand .brand-name { color: var(--ink); font-size: 30px; }
  .web-address {
    position: absolute; right: 28px; bottom: 76px;
    font-size: 12px; color: var(--paper);
    letter-spacing: 0.2px;
  }
</style>
</head>
<body>

<section class="card card-front" aria-label="Card front">
  <div class="brand-lockup">
    <span class="brand-marker" aria-hidden="true"></span>
    <div class="brand-text">
      <p class="brand-name">Veltrane Inc.</p>
      <p class="brand-sub">FLOORING &amp; CONCRETE REPAIR</p>
    </div>
  </div>
  <p class="front-tagline">WE'LL BE OUTSTANDING ON YOUR FLOORS</p>
</section>

<section class="card card-back" aria-label="Card back">
  <svg class="swoosh" viewBox="0 0 540 309" aria-hidden="true">
    <path d="M0,258 C170,262 360,220 540,122 L540,140 C370,236 180,276 0,276 Z" fill="var(--stripe)"/>
    <path d="M0,282 C190,284 380,240 540,146 L540,309 L0,309 Z" fill="var(--charcoal)"/>
  </svg>

  <p class="contact-name">MARC HOLLOWAY</p>
  <p class="contact-tollfree">1-800-555-0142</p>
  <p class="contact-address">PO Box 42 Ardenfield<br>WA 98000</p>
  <ul class="contact-list">
    <li><svg viewBox="0 0 16 16"><path d="M2 6c0-2 2-3 6-3s6 1 6 3v1h-3V6H5v1H2z M4 8h8l2 5H2z"/></svg>(360) 555-0131</li>
    <li><svg viewBox="0 0 16 16"><path d="M4 1h8v14H4z M5.5 2.5v9h5v-9z" fill-rule="evenodd"/></svg>(360) 555-0177</li>
    <li><svg viewBox="0 0 16 16"><path d="M4 1h8v4H4z M1 6h14v6h-3v3H4v-3H1z M5 10v3h6v-3z" fill-rule="evenodd"/></svg>(360) 555-0133</li>
    <li><svg viewBox="0 0 16 16"><path d="M1 3h14v10H1z M2 4.5v.3l6 4 6-4v-.3z" fill-rule="evenodd"/></svg>marc@veltranefloors.com</li>
  </ul>

  <div class="back-brand">
    <span class="brand-marker" aria-hidden="true"></span>
    <p class="brand-name">Veltrane Inc.</p>
  </div>

  <p class="web-address">www.veltranefloors.com</p>
</section>

</body>
</html>
```